Meridian Rest Supply Needs Business Card

Looking for a very nice looking business card. Creative but not extravagant. We sell beds and pillows across the U.S. and need something professional but catchy. I have attached the logo.

Name : Dale Fenwick
Title : President
Phone : (800) 417-2964
Email: sleep@quorvana.com
Website: www.quorvana.com

Can be single-sided or double-sided
horizontal or vertical

Can use Blues/Greys

Target Market(s)

Mass Market

Industry/Entity Type

Retail

Contact Information for Business Card

Name : Dale Fenwick
Title : President
Phone : (800) 417-2964
Email: sleep@quorvana.com
Website: www.quorvana.com

Requirements
Must have
• Clean, Modern, Smooth
• Can use Blues/Greys
• On the other side without the information - have something simple like www.quorvana.com or our logo
Nice to have
• Surprise me
Should not have
• Nothing crazy, nothing cluttered

```html
<!DOCTYPE html>
<html lang="en">
<head>
<meta charset="utf-8">
<title>Quorvana Business Card</title>
<link rel="stylesheet" href="https://fonts.googleapis.com/css2?family=Quicksand:wght@400;500&family=Courier+Prime&display=swap">
<style>
  :root {
    --backdrop: #7d8285;
    --card-deep: #0f272e;
    --card-mid: #163740;
    --groove: rgba(6, 20, 24, 0.75);
    --fibre-light: rgba(255, 255, 255, 0.018);
    --fibre-dark: rgba(0, 0, 0, 0.05);
    --ink-light: #ffffff;
  }
  html, body {
    margin: 0;
    padding: 0;
    width: 1200px;
    height: 1200px;
    overflow: hidden;
    background: var(--backdrop);
  }
  .canvas {
    position: relative;
    width: 1200px;
    height: 1200px;
  }
  .card {
    position: absolute;
    left: 178px;
    width: 841px;
    height: 481px;
    background:
      repeating-linear-gradient(135deg, var(--fibre-light) 0 1px, transparent 1px 3px),
      repeating-linear-gradient(45deg, var(--fibre-dark) 0 1px, transparent 1px 4px),
      radial-gradient(ellipse at 50% 50%, var(--card-mid) 0%, var(--card-deep) 85%);
    overflow: hidden;
  }
  .card--front { top: 110px; }
  .card--back { top: 618px; }
  .groove {
    position: absolute;
    left: 220px;
    width: 400px;
    height: 2px;
    background: linear-gradient(90deg, transparent, var(--groove) 20%, var(--groove) 80%, transparent);
  }
  .groove--top { top: 32px; }
  .groove--bottom { bottom: 33px; }
  .brand-name {
    position: absolute;
    left: 0;
    right: 0;
    top: 200px;
    margin: 0;
    text-align: center;
    font-family: "Quicksand", sans-serif;
    font-weight: 500;
    font-size: 60px;
    line-height: 70px;
    color: var(--ink-light);
  }
  .identity {
    position: absolute;
    right: 481px;
    top: 200px;
    text-align: right;
  }
  .identity__name {
    margin: 0;
    font-family: "Quicksand", sans-serif;
    font-weight: 500;
    font-size: 40px;
    line-height: 44px;
    color: var(--ink-light);
  }
  .identity__title {
    margin: 0;
    font-family: "Courier Prime", monospace;
    font-size: 25px;
    line-height: 26px;
    letter-spacing: 2px;
    color: var(--ink-light);
  }
  .divider {
    position: absolute;
    left: 396px;
    top: 154px;
    width: 2px;
    height: 172px;
    background: linear-gradient(180deg, transparent, var(--groove) 20%, var(--groove) 80%, transparent);
  }
  .contacts {
    position: absolute;
    left: 426px;
    top: 196px;
    margin: 0;
    padding: 0;
    list-style: none;
    font-family: "Quicksand", sans-serif;
    font-weight: 500;
    font-size: 26px;
    color: var(--ink-light);
  }
  .contacts__item {
    display: flex;
    align-items: center;
    height: 33px;
  }
  .contacts__icon {
    width: 26px;
    height: 22px;
    margin-right: 10px;
    flex: none;
  }
</style>
</head>
<body>
<main class="canvas">
  <section class="card card--front">
    <div class="groove groove--top"></div>
    <h1 class="brand-name">quorvana</h1>
    <div class="groove groove--bottom"></div>
  </section>

  <section class="card card--back">
    <div class="groove groove--top"></div>
    <div class="identity">
      <p class="identity__name">Dale Fenwick</p>
      <p class="identity__title">President</p>
    </div>
    <div class="divider"></div>
    <ul class="contacts">
      <li class="contacts__item">
        <svg class="contacts__icon" viewBox="0 0 26 22" aria-hidden="true">
          <path d="M2 8 Q13 0 24 8 L21 10 L18 7 Q13 5 8 7 L5 10 Z" fill="#fff"/>
          <rect x="6" y="11" width="14" height="9" rx="1.5" fill="#fff"/>
          <g fill="#163740">
            <rect x="8" y="13" width="2" height="2"/><rect x="12" y="13" width="2" height="2"/><rect x="16" y="13" width="2" height="2"/>
            <rect x="8" y="16.5" width="2" height="2"/><rect x="12" y="16.5" width="2" height="2"/><rect x="16" y="16.5" width="2" height="2"/>
          </g>
        </svg>
        <span>(800) 417-2964</span>
      </li>
      <li class="contacts__item">
        <svg class="contacts__icon" viewBox="0 0 26 22" aria-hidden="true">
          <rect x="2" y="2" width="22" height="18" rx="4" fill="#fff"/>
          <rect x="6" y="7" width="14" height="9" fill="#163740"/>
          <path d="M6 7 L13 12 L20 7" stroke="#fff" stroke-width="2" fill="none"/>
        </svg>
        <span>sleep@quorvana.com</span>
      </li>
      <li class="contacts__item">
        <svg class="contacts__icon" viewBox="0 0 26 22" aria-hidden="true">
          <circle cx="13" cy="11" r="9" stroke="#fff" stroke-width="2" fill="none"/>
          <ellipse cx="13" cy="11" rx="4" ry="9" stroke="#fff" stroke-width="1.6" fill="none"/>
          <line x1="4" y1="11" x2="22" y2="11" stroke="#fff" stroke-width="1.6"/>
        </svg>
        <span>www.quorvana.com</span>
      </li>
    </ul>
    <div class="groove groove--bottom"></div>
  </section>
</main>
</body>
</html>
```